Fahrzeugbeschriftung für Produktionsfirma
Zielgruppe
Wir sind eine Produktionsfirma und unterstützen unsere Kunden beim Design. Das Design soll aufmerksamkeitstärker umgesetzt werden. Ggf. auch mit einem Vollbranding. Die Farben sollen so bleiben.
Aufgabenstellung
Die Flotte von ca. 1500 Fahrzeugen soll sehr markant im Markt unterwegs sein.

```html
<!DOCTYPE html>
<html lang="de">
<head>
<meta charset="utf-8">
<title>Voltaro – Fahrzeugbeschriftung</title>
<link href="https://fonts.googleapis.com/css2?family=Open+Sans:wght@600;700&display=swap" rel="stylesheet">
<style>
  :root {
    --navy: #1b3566;
    --navy-dark: #132850;
    --yellow: #f6c21a;
    --trim: #1d1f23;
    --glass: #2a3440;
    --rim: #c9ced4;
    --hub: #8b929a;
    --tyre: #16181b;
    --headlight: #dfe6ee;
    --tail: #c8202a;
    --canvas: #f2f3f5;
    --white: #ffffff;
  }
  html, body {
    margin: 0;
    padding: 0;
    width: 1200px;
    height: 588px;
    overflow: hidden;
    background: var(--canvas);
  }
  .vehicle-wrap {
    position: relative;
    width: 1200px;
    height: 588px;
  }
  .vehicle-wrap svg {
    position: absolute;
    inset: 0;
  }
  .brand-name {
    position: absolute;
    left: 572px;
    top: 160px;
    margin: 0;
    font-family: "Open Sans", sans-serif;
    font-weight: 700;
    font-size: 78px;
    line-height: 1;
    color: var(--white);
    letter-spacing: 1px;
  }
  .claim {
    position: absolute;
    left: 402px;
    top: 322px;
    margin: 0;
    font-family: "Open Sans", sans-serif;
    font-weight: 600;
    font-size: 14px;
    line-height: 1.3;
    color: var(--white);
  }
  .web-address {
    position: absolute;
    left: 606px;
    top: 336px;
    margin: 0;
    font-family: "Open Sans", sans-serif;
    font-weight: 700;
    font-size: 16px;
    color: var(--navy-dark);
  }
</style>
</head>
<body>
<div class="vehicle-wrap">
  <svg viewBox="0 0 1200 588" width="1200" height="588">
    <defs>
      <clipPath id="body-shape">
        <path d="M162 455 L164 395 Q168 358 190 346 L330 248 Q380 150 470 108 Q490 98 520 97 L995 91 Q1025 91 1032 110 L1036 428 L162 455 Z"/>
      </clipPath>
      <linearGradient id="photo-tone" x1="0" y1="0" x2="1" y2="1">
        <stop offset="0" stop-color="#dfe4ea"/>
        <stop offset="0.45" stop-color="#4a6fa8"/>
        <stop offset="1" stop-color="#223c6c"/>
      </linearGradient>
    </defs>

    <g class="body-panels" clip-path="url(#body-shape)">
      <rect class="panel-navy" x="150" y="80" width="900" height="380" fill="var(--navy)"/>
      <polygon class="band-yellow" points="783,90 918,90 752,385 545,385" fill="var(--yellow)"/>
      <polygon class="rear-photo" points="918,90 1040,90 1040,385 752,385" fill="url(#photo-tone)" role="img" aria-label="Foto: Monteur installiert Solarmodule auf einem Dach"/>
      <rect class="lower-trim" x="150" y="385" width="900" height="75" fill="var(--trim)"/>
      <polygon class="sill-yellow" points="520,408 752,408 748,428 512,428" fill="var(--yellow)"/>
    </g>

    <path class="windshield" d="M196 346 L330 250 Q350 212 372 186 L360 300 Z" fill="var(--glass)"/>
    <path class="side-window" d="M378 186 Q400 170 430 168 L512 170 L512 282 L372 288 Z" fill="var(--glass)"/>
    <rect class="headlight" x="180" y="328" width="36" height="18" rx="6" fill="var(--headlight)"/>
    <rect class="tail-light" x="1004" y="270" width="14" height="92" rx="3" fill="var(--tail)"/>
    <rect class="mirror" x="358" y="244" width="14" height="34" rx="4" fill="var(--trim)"/>

    <g class="wheels">
      <circle cx="328" cy="447" r="58" fill="var(--tyre)"/>
      <circle cx="328" cy="447" r="36" fill="var(--rim)"/>
      <circle cx="328" cy="447" r="8" fill="var(--hub)"/>
      <circle cx="862" cy="445" r="58" fill="var(--tyre)"/>
      <circle cx="862" cy="445" r="36" fill="var(--rim)"/>
      <circle cx="862" cy="445" r="8" fill="var(--hub)"/>
    </g>
  </svg>

  <h1 class="brand-name">Voltaro</h1>
  <p class="claim">Dein Dach,<br>deine Kraft.</p>
  <p class="web-address">www.voltaro.de</p>
</div>
</body>
</html>
```